Need modern simple design for magazine ad, apartment and condo roofer.

I need a half page magazine ad for a local roofer to publish in an industry magazine. Apartment associations industry. All types of roofs. Shingle and Flat
Need the design to be creative and modern, clean and simple. I do not want a busy design. One that stands out and makes a point quickly.
Logo must be prominent.
DO NOT USE PHOTOS FROM MY WEBSITE PLEASE. Looking for something new.
I work on entire complexes not houses.

Need to make sure our phone number and email address are listed at the bottom. Here is my website www.vorbelan.com
Want to stay away from standard clip arts of tools, homes, apartment buildings.
Half Horizontal 7.25 x 4.75
Ads should be in PDF and JPG format.

Target Market(s)

Apartment or Condo owners looking for large scale roofing projects

Industry/Entity Type

Roofing

Requirements
Must have
• Prominent Logo
Simple Clean Design
Create graphics
Not Busy
Should not have
• Clip Art
No Photos from my website

```html
<!DOCTYPE html>
<html lang="en">
<head>
<meta charset="utf-8">
<title>Vorbelan Roofing – Half Page Ad</title>
<link rel="stylesheet" href="https://fonts.googleapis.com/css2?family=Arimo:wght@400;700&family=Oswald:wght@600&family=Roboto:wght@400;500&display=swap">
<style>
  :root {
    --stage: #454547;
    --blue: #1f7fc9;
    --blue-bright: #2a8fdc;
    --ink: #111214;
    --paper: #ffffff;
    --steel: #9a9c9f;
    --steel-dark: #6f7174;
    --text-dark: #1b1b1b;
    --badge-navy: #1d3b73;
    --badge-red: #c8242f;
    --badge-teal: #2d6b86;
  }
  * { margin: 0; padding: 0; box-sizing: border-box; }
  html, body { width: 866px; height: 1200px; overflow: hidden; }
  body { background: var(--stage); position: relative; font-family: "Roboto", Arial, sans-serif; }

  .ad {
    position: absolute; left: 112px; width: 642px; height: 421px;
    box-shadow: 0 6px 14px rgba(0,0,0,.45);
    overflow: hidden;
  }
  .ad--dark { top: 154px; background: linear-gradient(180deg, #050607 0%, var(--ink) 100%); color: var(--paper); }
  .ad--light { top: 627px; background: var(--paper); color: var(--text-dark); }

  .side-band {
    position: absolute; left: 0; top: 0; width: 66px; height: 315px;
    background: var(--blue);
    display: flex; align-items: center; justify-content: center;
  }
  .side-band span {
    transform: rotate(-90deg); white-space: nowrap;
    font-family: "Oswald", "Arial Narrow", sans-serif; font-weight: 600;
    font-size: 25px; letter-spacing: .5px; color: var(--paper);
  }

  .brand { position: absolute; left: 108px; top: 16px; display: flex; align-items: center; gap: 14px; }
  .brand-mark { width: 48px; height: 48px; background: var(--blue); }
  .brand-text { display: flex; flex-direction: column; }
  .brand-name {
    font-family: "Arimo", Arial, sans-serif; font-weight: 700; font-size: 62px;
    line-height: 1; color: var(--steel); letter-spacing: 1px;
  }
  .brand-tagline {
    font-family: "Arimo", Arial, sans-serif; font-weight: 700; font-size: 21px;
    color: var(--blue); margin-top: 4px; text-align: right;
  }

  .services { position: absolute; top: 146px; list-style: none; font-size: 18px; line-height: 23.7px; }
  .services--left { left: 93px; }
  .services--right { left: 365px; }
  .services li { display: flex; align-items: center; gap: 6px; white-space: nowrap; }
  .services li.more { padding-left: 20px; }
  .services .more-link { color: var(--blue-bright); }
  .tick { width: 14px; height: 14px; flex: none; }

  .phone {
    position: absolute; left: 14px; top: 320px; display: flex; align-items: center; gap: 8px;
    font-family: "Arimo", Arial, sans-serif; font-weight: 700; font-size: 25px; color: var(--blue);
  }
  .phone svg { width: 16px; height: 24px; }

  .contact-box {
    position: absolute; left: 0; top: 350px; width: 248px; height: 71px;
    background: var(--blue); color: var(--paper);
    padding: 6px 0 0 14px; font-size: 17px; line-height: 25px;
  }
  .contact-box div { display: flex; align-items: center; gap: 12px; }
  .contact-box svg { width: 18px; height: 18px; flex: none; }

  .memberships {
    position: absolute; left: 248px; top: 322px; width: 394px; height: 99px;
    background: var(--paper);
  }
  .memberships svg { width: 100%; height: 100%; }
</style>
</head>
<body>

<!-- Dark version -->
<section class="ad ad--dark">
  <div class="side-band"><span>GENERAL CONTRACTOR</span></div>

  <div class="brand">
    <div class="brand-mark"></div>
    <div class="brand-text">
      <div class="brand-name">VORBELAN</div>
      <div class="brand-tagline">Multifamily Roofing</div>
    </div>
  </div>

  <ul class="services services--left">
    <li><svg class="tick" viewBox="0 0 14 14"><rect x=".5" y=".5" width="13" height="13" fill="#9fc9ea" stroke="#1f7fc9"/><path d="M3 7l3 3 5-6" fill="none" stroke="#1f7fc9" stroke-width="2"/></svg>Fire Restoration</li>
    <li><svg class="tick" viewBox="0 0 14 14"><rect x=".5" y=".5" width="13" height="13" fill="#9fc9ea" stroke="#1f7fc9"/><path d="M3 7l3 3 5-6" fill="none" stroke="#1f7fc9" stroke-width="2"/></svg>Due Diligence</li>
    <li><svg class="tick" viewBox="0 0 14 14"><rect x=".5" y=".5" width="13" height="13" fill="#9fc9ea" stroke="#1f7fc9"/><path d="M3 7l3 3 5-6" fill="none" stroke="#1f7fc9" stroke-width="2"/></svg>Exterior Renovations</li>
    <li><svg class="tick" viewBox="0 0 14 14"><rect x=".5" y=".5" width="13" height="13" fill="#9fc9ea" stroke="#1f7fc9"/><path d="M3 7l3 3 5-6" fill="none" stroke="#1f7fc9" stroke-width="2"/></svg>Siding / Wood Replacement</li>
    <li><svg class="tick" viewBox="0 0 14 14"><rect x=".5" y=".5" width="13" height="13" fill="#9fc9ea" stroke="#1f7fc9"/><path d="M3 7l3 3 5-6" fill="none" stroke="#1f7fc9" stroke-width="2"/></svg>Full Paint</li>
    <li><svg class="tick" viewBox="0 0 14 14"><rect x=".5" y=".5" width="13" height="13" fill="#9fc9ea" stroke="#1f7fc9"/><path d="M3 7l3 3 5-6" fill="none" stroke="#1f7fc9" stroke-width="2"/></svg>Roofing (all types)</li>
    <li><svg class="tick" viewBox="0 0 14 14"><rect x=".5" y=".5" width="13" height="13" fill="#9fc9ea" stroke="#1f7fc9"/><path d="M3 7l3 3 5-6" fill="none" stroke="#1f7fc9" stroke-width="2"/></svg>Balcony/Landing Repairs</li>
  </ul>
  <ul class="services services--right">
    <li><svg class="tick" viewBox="0 0 14 14"><rect x=".5" y=".5" width="13" height="13" fill="#9fc9ea" stroke="#1f7fc9"/><path d="M3 7l3 3 5-6" fill="none" stroke="#1f7fc9" stroke-width="2"/></svg>Concrete</li>
    <li><svg class="tick" viewBox="0 0 14 14"><rect x=".5" y=".5" width="13" height="13" fill="#9fc9ea" stroke="#1f7fc9"/><path d="M3 7l3 3 5-6" fill="none" stroke="#1f7fc9" stroke-width="2"/></svg>Brick/Stucco/Masonry</li>
    <li><svg class="tick" viewBox="0 0 14 14"><rect x=".5" y=".5" width="13" height="13" fill="#9fc9ea" stroke="#1f7fc9"/><path d="M3 7l3 3 5-6" fill="none" stroke="#1f7fc9" stroke-width="2"/></svg>Carports / Metal Fencing</li>
    <li><svg class="tick" viewBox="0 0 14 14"><rect x=".5" y=".5" width="13" height="13" fill="#9fc9ea" stroke="#1f7fc9"/><path d="M3 7l3 3 5-6" fill="none" stroke="#1f7fc9" stroke-width="2"/></svg>Disaster Restoration</li>
    <li><svg class="tick" viewBox="0 0 14 14"><rect x=".5" y=".5" width="13" height="13" fill="#9fc9ea" stroke="#1f7fc9"/><path d="M3 7l3 3 5-6" fill="none" stroke="#1f7fc9" stroke-width="2"/></svg>Interior Renovations</li>
    <li><svg class="tick" viewBox="0 0 14 14"><rect x=".5" y=".5" width="13" height="13" fill="#9fc9ea" stroke="#1f7fc9"/><path d="M3 7l3 3 5-6" fill="none" stroke="#1f7fc9" stroke-width="2"/></svg>Leasing Office Renovations</li>
    <li class="more">and&nbsp;<span class="more-link">more. . .</span></li>
  </ul>

  <div class="phone">
    <svg viewBox="0 0 16 24"><path d="M5 2h3l1 6-3 2q0 4 3 6l3-2 1 6h-3Q3 18 5 2z" fill="currentColor"/></svg>
    555.214.0387
  </div>

  <div class="contact-box">
    <div><svg viewBox="0 0 18 18"><rect x="1" y="3" width="16" height="12" fill="none" stroke="#fff" stroke-width="1.6"/><path d="M1 3l8 7 8-7" fill="none" stroke="#fff" stroke-width="1.6"/></svg>info@vorbelan.com</div>
    <div><svg viewBox="0 0 18 18"><circle cx="9" cy="9" r="8" fill="none" stroke="#fff" stroke-width="1.6"/><ellipse cx="9" cy="9" rx="3.5" ry="8" fill="none" stroke="#fff" stroke-width="1.3"/><path d="M1 9h16M2.5 5h13M2.5 13h13" stroke="#fff" stroke-width="1.2"/></svg>www.vorbelan.com</div>
  </div>

  <div class="memberships" role="img" aria-label="Membership and accreditation badges">
    <svg viewBox="0 0 394 99">
      <rect x="22" y="18" width="56" height="62" fill="var(--badge-navy)"/>
      <circle cx="124" cy="48" r="26" fill="var(--badge-navy)"/>
      <circle cx="185" cy="48" r="28" fill="none" stroke="var(--badge-red)" stroke-width="5"/>
      <rect x="240" y="12" width="110" height="26" fill="var(--badge-navy)"/>
      <rect x="240" y="46" width="64" height="34" rx="3" fill="var(--badge-teal)"/>
      <rect x="312" y="50" width="40" height="26" fill="#d7dde3"/>
    </svg>
  </div>
</section>

<!-- Light version -->
<section class="ad ad--light">
  <div class="side-band"><span>GENERAL CONTRACTOR</span></div>

  <div class="brand">
    <div class="brand-mark"></div>
    <div class="brand-text">
      <div class="brand-name">VORBELAN</div>
      <div class="brand-tagline">Multifamily Roofing</div>
    </div>
  </div>

  <ul class="services services--left">
    <li><svg class="tick" viewBox="0 0 14 14"><rect x=".5" y=".5" width="13" height="13" fill="#9fc9ea" stroke="#1f7fc9"/><path d="M3 7l3 3 5-6" fill="none" stroke="#1f7fc9" stroke-width="2"/></svg>Fire Restoration</li>
    <li><svg class="tick" viewBox="0 0 14 14"><rect x=".5" y=".5" width="13" height="13" fill="#9fc9ea" stroke="#1f7fc9"/><path d="M3 7l3 3 5-6" fill="none" stroke="#1f7fc9" stroke-width="2"/></svg>Due Diligence</li>
    <li><svg class="tick" viewBox="0 0 14 14"><rect x=".5" y=".5" width="13" height="13" fill="#9fc9ea" stroke="#1f7fc9"/><path d="M3 7l3 3 5-6" fill="none" stroke="#1f7fc9" stroke-width="2"/></svg>Exterior Renovations</li>
    <li><svg class="tick" viewBox="0 0 14 14"><rect x=".5" y=".5" width="13" height="13" fill="#9fc9ea" stroke="#1f7fc9"/><path d="M3 7l3 3 5-6" fill="none" stroke="#1f7fc9" stroke-width="2"/></svg>Siding / Wood Replacement</li>
    <li><svg class="tick" viewBox="0 0 14 14"><rect x=".5" y=".5" width="13" height="13" fill="#9fc9ea" stroke="#1f7fc9"/><path d="M3 7l3 3 5-6" fill="none" stroke="#1f7fc9" stroke-width="2"/></svg>Full Paint</li>
    <li><svg class="tick" viewBox="0 0 14 14"><rect x=".5" y=".5" width="13" height="13" fill="#9fc9ea" stroke="#1f7fc9"/><path d="M3 7l3 3 5-6" fill="none" stroke="#1f7fc9" stroke-width="2"/></svg>Roofing (all types)</li>
    <li><svg class="tick" viewBox="0 0 14 14"><rect x=".5" y=".5" width="13" height="13" fill="#9fc9ea" stroke="#1f7fc9"/><path d="M3 7l3 3 5-6" fill="none" stroke="#1f7fc9" stroke-width="2"/></svg>Balcony/Landing Repairs</li>
  </ul>
  <ul class="services services--right">
    <li><svg class="tick" viewBox="0 0 14 14"><rect x=".5" y=".5" width="13" height="13" fill="#9fc9ea" stroke="#1f7fc9"/><path d="M3 7l3 3 5-6" fill="none" stroke="#1f7fc9" stroke-width="2"/></svg>Concrete</li>
    <li><svg class="tick" viewBox="0 0 14 14"><rect x=".5" y=".5" width="13" height="13" fill="#9fc9ea" stroke="#1f7fc9"/><path d="M3 7l3 3 5-6" fill="none" stroke="#1f7fc9" stroke-width="2"/></svg>Brick/Stucco/Masonry</li>
    <li><svg class="tick" viewBox="0 0 14 14"><rect x=".5" y=".5" width="13" height="13" fill="#9fc9ea" stroke="#1f7fc9"/><path d="M3 7l3 3 5-6" fill="none" stroke="#1f7fc9" stroke-width="2"/></svg>Carports / Metal Fencing</li>
    <li><svg class="tick" viewBox="0 0 14 14"><rect x=".5" y=".5" width="13" height="13" fill="#9fc9ea" stroke="#1f7fc9"/><path d="M3 7l3 3 5-6" fill="none" stroke="#1f7fc9" stroke-width="2"/></svg>Disaster Restoration</li>
    <li><svg class="tick" viewBox="0 0 14 14"><rect x=".5" y=".5" width="13" height="13" fill="#9fc9ea" stroke="#1f7fc9"/><path d="M3 7l3 3 5-6" fill="none" stroke="#1f7fc9" stroke-width="2"/></svg>Interior Renovations</li>
    <li><svg class="tick" viewBox="0 0 14 14"><rect x=".5" y=".5" width="13" height="13" fill="#9fc9ea" stroke="#1f7fc9"/><path d="M3 7l3 3 5-6" fill="none" stroke="#1f7fc9" stroke-width="2"/></svg>Leasing Office Renovations</li>
    <li class="more">and&nbsp;<span class="more-link">more. . .</span></li>
  </ul>

  <div class="phone">
    <svg viewBox="0 0 16 24"><path d="M5 2h3l1 6-3 2q0 4 3 6l3-2 1 6h-3Q3 18 5 2z" fill="#111214"/></svg>
    555.214.0387
  </div>

  <div class="contact-box">
    <div><svg viewBox="0 0 18 18"><rect x="1" y="3" width="16" height="12" fill="none" stroke="#fff" stroke-width="1.6"/><path d="M1 3l8 7 8-7" fill="none" stroke="#fff" stroke-width="1.6"/></svg>info@vorbelan.com</div>
    <div><svg viewBox="0 0 18 18"><circle cx="9" cy="9" r="8" fill="none" stroke="#fff" stroke-width="1.6"/><ellipse cx="9" cy="9" rx="3.5" ry="8" fill="none" stroke="#fff" stroke-width="1.3"/><path d="M1 9h16M2.5 5h13M2.5 13h13" stroke="#fff" stroke-width="1.2"/></svg>www.vorbelan.com</div>
  </div>

  <div class="memberships" role="img" aria-label="Membership and accreditation badges">
    <svg viewBox="0 0 394 99">
      <rect x="22" y="18" width="56" height="62" fill="var(--badge-navy)"/>
      <circle cx="124" cy="48" r="26" fill="var(--badge-navy)"/>
      <circle cx="185" cy="48" r="28" fill="none" stroke="var(--badge-red)" stroke-width="5"/>
      <rect x="240" y="12" width="110" height="26" fill="var(--badge-navy)"/>
      <rect x="240" y="46" width="64" height="34" rx="3" fill="var(--badge-teal)"/>
      <rect x="312" y="50" width="40" height="26" fill="#d7dde3"/>
    </svg>
  </div>
</section>

</body>
</html>
```